Corvane Nightclub Flyer (Updated)

Flyer for facebook, square is fine, or rectangular. Here is the text:
CORVANE
Nightclub + Lounge
presents

HALO THURSDAY
Nov 29 2018

CLUB FLOOR:
GLEN B2B ROBBY
FREDERICK TALAVERO

LOUNGE:
CARL B2B MY COUSIN
ROCKET JULES

Powered by KESTA Acoustics
4217 6th Street 21+ 9pm-2am
corvanevenuehall.com for VIP booth inquiries

Target Market(s)

Nightclub

Industry/Entity Type

Night Club

Font styles to use
Sans Serif

Colors

Designer to choose colors to be used in the design.

Requirements
Must have
• All the text listed, and plz keep the theme of the attached files. We want to stay consistent with the Corvane brand
Nice to have
• Try to stay with the theme from the attachments
Should not have
• Dont' stray to far from the general theme we have from the attachments

```html
<!DOCTYPE html>
<html lang="en">
<head>
<meta charset="utf-8">
<title>Corvane Nightclub + Lounge — Halo Thursday</title>
<link href="https://fonts.googleapis.com/css2?family=Bebas+Neue&family=Open+Sans:wght@300;400;600;700&display=swap" rel="stylesheet">
<style>
  :root {
    --bg: #0a0a0a;
    --bg-soft: #141312;
    --band: rgba(48, 44, 40, 0.55);
    --white: #ffffff;
    --gold: #b8874b;
    --gold-light: #d6a866;
    --gold-deep: #6e4e26;
  }
  * { margin: 0; padding: 0; box-sizing: border-box; }
  html, body {
    width: 1200px; height: 847px; overflow: hidden;
    background: var(--bg);
  }
  .flyer {
    position: relative;
    width: 1200px; height: 847px; overflow: hidden;
    background: radial-gradient(ellipse at 40% 40%, var(--bg-soft) 0%, var(--bg) 70%);
    font-family: "Open Sans", sans-serif;
    color: var(--white);
  }
  .ornament {
    position: absolute; left: 620px; top: 420px;
    width: 600px; height: 440px;
  }
  .brand { position: absolute; left: 79px; top: 62px; }
  .brand-name {
    font-weight: 300; font-size: 118px; line-height: 1;
    letter-spacing: 2px;
  }
  .brand-tagline {
    margin-top: 26px; margin-left: 4px;
    font-weight: 300; font-size: 34px; line-height: 1;
    letter-spacing: 9px;
  }
  .presents {
    position: absolute; left: 693px; top: 118px;
    font-size: 20px; letter-spacing: 1px;
  }
  .event {
    position: absolute; right: 74px; top: 62px;
    text-align: right;
  }
  .event-title {
    font-family: "Bebas Neue", sans-serif;
    font-size: 222px; line-height: 0.9; letter-spacing: -2px;
  }
  .event-day {
    margin-top: 4px;
    font-size: 55px; line-height: 1.05; font-weight: 400;
  }
  .event-date {
    font-size: 48px; line-height: 1.05; font-weight: 700;
    color: var(--gold);
  }
  .band {
    position: absolute; left: 0; width: 820px; height: 144px;
    background: linear-gradient(90deg, var(--band) 0%, var(--band) 70%, rgba(48,44,40,0) 100%);
    padding: 14px 0 0 78px;
  }
  .band--club { top: 298px; }
  .band--lounge { top: 449px; }
  .band-label {
    font-weight: 700; font-size: 28px; line-height: 40px;
    color: var(--gold);
  }
  .band-headliner { font-weight: 700; font-size: 28px; line-height: 40px; }
  .band-support { font-weight: 400; font-size: 28px; line-height: 40px; }
  .info { position: absolute; left: 78px; top: 658px; }
  .powered {
    font-size: 32px; font-weight: 400; line-height: 1.2;
    padding-bottom: 4px;
    border-bottom: 1px solid var(--gold);
    width: 433px;
  }
  .powered-lead { color: var(--gold); font-weight: 300; }
  .details {
    margin-top: 14px;
    font-size: 20px; line-height: 28px;
  }
  .details .vip { color: var(--gold); font-weight: 700; }
</style>
</head>
<body>
<main class="flyer">
  <svg class="ornament" role="img" aria-label="Gold ornamental mandala decoration rising from the lower right corner" viewBox="0 0 600 440">
    <defs>
      <radialGradient id="mandala-glow" cx="70%" cy="85%" r="75%">
        <stop offset="0%" stop-color="#d6a866" stop-opacity="0.75"/>
        <stop offset="45%" stop-color="#8a6232" stop-opacity="0.45"/>
        <stop offset="100%" stop-color="#0a0a0a" stop-opacity="0"/>
      </radialGradient>
    </defs>
    <ellipse cx="420" cy="440" rx="420" ry="330" fill="url(#mandala-glow)"/>
  </svg>

  <header class="brand">
    <div class="brand-name">CORVANE</div>
    <div class="brand-tagline">NIGHTCLUB + LOUNGE</div>
  </header>

  <div class="presents">PRESENTS</div>

  <section class="event">
    <div class="event-title">HALO</div>
    <div class="event-day">THURSDAY</div>
    <div class="event-date">Nov 29 2018</div>
  </section>

  <section class="band band--club">
    <div class="band-label">CLUB FLOOR:</div>
    <div class="band-headliner">GLEN B2B ROBBY</div>
    <div class="band-support">FREDERICK TALAVERO</div>
  </section>

  <section class="band band--lounge">
    <div class="band-label">LOUNGE:</div>
    <div class="band-headliner">CARL B2B MY COUSIN</div>
    <div class="band-support">ROCKET JULES</div>
  </section>

  <footer class="info">
    <div class="powered"><span class="powered-lead">Powered</span> by KESTA Acoustics</div>
    <div class="details">
      <div>4217 6th Street 21+ 9pm-2am</div>
      <div>corvanevenuehall.com for <span class="vip">VIP</span> booth inquiries</div>
    </div>
  </footer>
</main>
</body>
</html>
```